new letterhead/envelope/business card design for law firm

please see attached pdf of current letterhead, envelope and business card. I am also attaching my new logo that I would like to be used. basically, I am looking to refresh and simplify my letterhead/stationary and business card, keeping the following in mind:

overall, I am going for the following look:

-simple,
-modern,
-classy,
-professional

Target Market(s)

law firm clients

Industry/Entity Type

Law Firm

Contact Information for Business Card

see attachment

Font styles to use
Sans Serif

Requirements
Must have
• overall, I am going for the following look:
• -simple,
• -modern,
• -classy,
• -professional
Nice to have
• same as above
Should not have
• no serif fonts

```html
<!DOCTYPE html>
<html lang="en">
<head>
<meta charset="utf-8">
<title>Hollis Law — Stationery</title>
<link href="https://fonts.googleapis.com/css2?family=Montserrat:wght@500;600;700&display=swap" rel="stylesheet">
<style>
  :root {
    --backdrop: #ecedec;
    --paper: #ffffff;
    --navy: #0c2a4d;
    --green: #43832f;
    --shadow: rgba(0, 0, 0, 0.12);
  }
  html, body {
    margin: 0;
    padding: 0;
    width: 1200px;
    height: 1200px;
    overflow: hidden;
    background: var(--backdrop);
    font-family: "Montserrat", Arial, sans-serif;
    color: var(--navy);
  }
  .sheet {
    position: absolute;
    background: var(--paper);
    box-shadow: 0 1px 4px var(--shadow);
  }
  /* Envelope */
  .envelope {
    left: 86px; top: 65px; width: 1028px; height: 658px;
    border-radius: 36px 36px 0 0;
    overflow: hidden;
  }
  .envelope-flap {
    position: absolute; left: 0; top: 0; width: 100%; height: 144px;
    background: var(--green);
  }
  .envelope-sender {
    position: absolute; left: 41px; top: 193px; width: 164px;
    text-align: center;
  }
  .mark-circle {
    display: block;
    border-radius: 50%;
    background: var(--navy);
  }
  .envelope-sender .mark-circle { width: 88px; height: 88px; margin: 0 auto; }
  .firm-name {
    font-weight: 700;
    color: var(--navy);
    letter-spacing: 0.5px;
    white-space: nowrap;
  }
  .envelope-sender .firm-name { font-size: 25px; margin-top: 12px; }
  .envelope-address {
    margin-top: 14px; font-size: 11px; line-height: 16px; font-weight: 500;
  }
  /* Business cards */
  .card { top: 835px; width: 516px; height: 299px; }
  .card-front { left: 71px; }
  .card-front .brand {
    position: absolute; left: 0; top: 0; width: 100%; height: 100%;
    display: flex; align-items: center; justify-content: center; gap: 16px;
  }
  .card-front .mark-circle { width: 74px; height: 74px; }
  .card-front .firm-name { font-size: 34px; }
  .card-back { left: 615px; }
  .card-back .brand {
    position: absolute; left: 36px; top: 76px; width: 200px; text-align: center;
  }
  .card-back .mark-circle { width: 96px; height: 96px; margin: 0 auto; }
  .card-back .firm-name { font-size: 28px; margin-top: 14px; }
  .card-details {
    position: absolute; right: 31px; top: 32px; text-align: right;
    font-size: 13px; font-weight: 500; line-height: 17px;
  }
  .attorney-name { font-size: 15px; font-weight: 700; letter-spacing: 0.4px; }
  .attorney-licence { color: var(--green); font-size: 14px; margin-top: 2px; }
  .contact-list { margin-top: 65px; }
  .contact-label { color: var(--green); margin-right: 5px; }
  .contact-address { margin-top: 14px; }
</style>
</head>
<body>

  <section class="sheet envelope" aria-label="Envelope">
    <div class="envelope-flap"></div>
    <div class="envelope-sender">
      <span class="mark-circle"></span>
      <div class="firm-name">HOLLIS LAW</div>
      <div class="envelope-address">
        2840 Larkspur Avenue, Suite 210<br>
        Raleigh, NC 27605
      </div>
    </div>
  </section>

  <section class="sheet card card-front" aria-label="Business card front">
    <div class="brand">
      <span class="mark-circle"></span>
      <span class="firm-name">HOLLIS LAW</span>
    </div>
  </section>

  <section class="sheet card card-back" aria-label="Business card back">
    <div class="brand">
      <span class="mark-circle"></span>
      <div class="firm-name">HOLLIS LAW</div>
    </div>
    <div class="card-details">
      <div class="attorney-name">DANIEL R. HOLLIS, ESQ</div>
      <div class="attorney-licence">Licensed in NC and FL</div>
      <div class="contact-list">
        <div><span class="contact-label">PHONE</span>919 555 0142</div>
        <div><span class="contact-label">FAX</span>919 555 0187</div>
        <div><span class="contact-label">CELL</span>919 555 0163</div>
        <div>dan@hollislawpa.com</div>
        <div>www.hollislawpa.com</div>
      </div>
      <div class="contact-address">
        2840 Larkspur Avenue, Suite 210<br>
        Raleigh, NC 27605
      </div>
    </div>
  </section>

</body>
</html>
```